Advertisement Design Project

We need a design for a new color newspaper print ad that can be sized 8.75 wide by 5.65 tall. You can also use the size: 4.29 wide x 11.50 tall.

We are targeting men's suit and men's accessories consumers. We sell men's suits, shirts, ties belts and shoes. We want the ad to be promotional and eye catching. Use color as needed

These are the items we want to have in the ad:

(The emphasis must be on the 3 suits for $99.99
3 Suits for $99.99
regular price $199.99

EXECUTIVE SUIT
FREEDOM PACKAGE
10 ITEMS for $199 includes:2 DESIGNER SUITS
2 FREE dress shirts
2 FREE matching ties
2 FREE leather belts
2 FREE dress socks

Headline:
SUMMER SAVINGS
3 DAYS ONLY!
Additional copy points:
1000’s of suits in stock
SIZES 34 SHORT - 60 LONG
Alterations done on premises
At bottom of the ad:
9TH & HOLLOWAY 267.555.0148
BRISTOW GATE PLAZA 215.555.0193
www.orvillemenswear.example
Not valid toward previous purchases. Offer may be cancelled and modified at any time.
Artists: See logo attached

If you saw this post yesterday, please disregard the image that was included with the brief. We have removed that image so you use your creativity to create a completely new ad for us.
Updates

Please use the attached image only as a guide. We would like to see unique, and creative designs for our print ads, a completely new look. We are looking for creativity here featuring the products so they pop

The emphasis in the ad must be on the 3 suits for $99.99
3 Suits for $99.99
regular price $199.99

Target Market(s)

Men's suit customers and men's apparel.

Industry/Entity Type

Artists

Requirements
Must have
• Eye catching The ad can should be sized 8.75 wide by 5.65 tall or the size: 4.29 wide x 11.50 tall.

```html
<!DOCTYPE html>
<html lang="en">
<head>
<meta charset="utf-8">
<title>Orville Menswear – Summer Savings</title>
<link rel="stylesheet" href="https://fonts.googleapis.com/css2?family=Montserrat:wght@300;400;500;600;700&display=swap">
<style>
  :root {
    --stage: #3a3a3a;
    --ink: #111111;
    --paper: #ffffff;
    --gold: #f3b443;
    --black: #000000;
    --muted: #8a8a8a;
    --rule: #cfcfcf;
    --photo-dark: #2b211c;
    --photo-mid: #6b4a35;
    --photo-warm: #a7754f;
  }
  * { margin: 0; padding: 0; box-sizing: border-box; }
  html, body { width: 1200px; height: 1000px; overflow: hidden; }
  body { background: var(--stage); font-family: "Montserrat", sans-serif; position: relative; }

  .ad { position: absolute; left: 51px; top: 63px; width: 1098px; height: 708px; background: var(--paper); overflow: hidden; }

  .hero-photo { position: absolute; left: 0; top: 0; width: 709px; height: 464px;
    background: linear-gradient(100deg, var(--photo-dark) 0%, var(--photo-mid) 35%, var(--photo-dark) 60%, var(--photo-warm) 85%, var(--photo-mid) 100%); }
  .hero-shade { position: absolute; left: 0; top: 185px; width: 709px; height: 279px; background: rgba(0,0,0,0.55); }

  .headline { position: absolute; left: 0; width: 709px; color: var(--gold); font-weight: 400; line-height: 1; white-space: nowrap; }
  .headline--summer { top: 200px; left: 46px; font-size: 100px; letter-spacing: 9px; }
  .headline--savings { top: 298px; left: 43px; font-size: 100px; letter-spacing: 6px; }
  .headline--days { top: 393px; left: 54px; font-size: 66px; letter-spacing: 5px; font-weight: 300; }

  .offer-band { position: absolute; left: 0; top: 464px; width: 709px; height: 244px; background: var(--black); color: var(--paper); }
  .offer { position: absolute; left: 52px; white-space: nowrap; line-height: 1; }
  .offer--lead { top: 24px; font-size: 34px; font-weight: 700; }
  .offer--lead-note { top: 68px; font-size: 21px; font-weight: 500; }
  .offer--italian { top: 121px; font-size: 26px; font-weight: 500; letter-spacing: 0.5px; }
  .offer--italian-price { top: 157px; font-size: 30px; font-weight: 700; }
  .offer--italian-note { top: 195px; font-size: 21px; font-weight: 500; }

  .package { position: absolute; left: 722px; top: 44px; color: var(--ink); }
  .package__title { font-size: 35px; font-weight: 300; line-height: 44px; white-space: nowrap; }
  .package__price { font-size: 35px; font-weight: 700; line-height: 44px; white-space: nowrap; }
  .package__includes { margin: 8px 0 0 24px; font-size: 21px; font-weight: 500; }
  .package__list { list-style: none; margin: 2px 0 0 36px; }
  .package__item { display: flex; align-items: center; gap: 12px; font-size: 22px; font-weight: 500; line-height: 28px; white-space: nowrap; }
  .package__tick { width: 16px; height: 16px; flex: none; }

  .rule { position: absolute; left: 740px; width: 340px; height: 1px; background: linear-gradient(90deg, transparent, var(--rule) 15%, var(--rule) 85%, transparent); }
  .rule--top { top: 375px; }
  .rule--bottom { top: 454px; }

  .stock { position: absolute; left: 740px; top: 387px; width: 340px; text-align: center; font-size: 16.5px; line-height: 21px; color: #333; }

  .brand { position: absolute; left: 522px; top: 497px; width: 249px; height: 140px; background: var(--paper); display: flex; flex-direction: column; align-items: center; justify-content: center; color: var(--ink); }
  .brand__name { font-size: 52px; font-weight: 500; line-height: 1; }
  .brand__sub { font-size: 32px; font-weight: 500; line-height: 1.1; }

  .divider { position: absolute; left: 789px; top: 502px; width: 2px; height: 182px; background: #555; }

  .contact { position: absolute; left: 805px; top: 500px; color: var(--ink); white-space: nowrap; }
  .contact__place { font-size: 18px; font-weight: 500; line-height: 22px; letter-spacing: 0.5px; }
  .contact__phone { font-size: 25px; font-weight: 600; line-height: 36px; letter-spacing: 0.5px; }
  .contact__web { font-size: 17px; font-weight: 600; line-height: 24px; }
  .contact__legal { font-size: 12.5px; font-weight: 500; line-height: 16px; color: var(--muted); }
</style>
</head>
<body>
  <section class="ad">
    <div class="hero-photo" role="img" aria-label="Mannequins dressed in black, brown and grey suits with vests and ties in a menswear store"></div>
    <div class="hero-shade"></div>
    <div class="headline headline--summer">SUMMER</div>
    <div class="headline headline--savings">SAVINGS</div>
    <div class="headline headline--days">3 DAYS ONLY!</div>

    <div class="offer-band">
      <div class="offer offer--lead">3 Suits for $99.99</div>
      <div class="offer offer--lead-note">regular price $199.99</div>
      <div class="offer offer--italian">ITALIAN DESIGNER SUITS</div>
      <div class="offer offer--italian-price">2 for $125</div>
      <div class="offer offer--italian-note">regular price $79.99</div>
    </div>

    <div class="package">
      <div class="package__title">EXECUTIVE SUIT</div>
      <div class="package__title">FREEDOM PACKAGE</div>
      <div class="package__price">10 ITEMS for $199</div>
      <div class="package__includes">Includes :</div>
      <ul class="package__list">
        <li class="package__item"><svg class="package__tick" viewBox="0 0 16 16"><path d="M2 9 L6 13 L14 3" fill="none" stroke="#111" stroke-width="1.6"/></svg>2 DESIGNER SUITS</li>
        <li class="package__item"><svg class="package__tick" viewBox="0 0 16 16"><path d="M2 9 L6 13 L14 3" fill="none" stroke="#111" stroke-width="1.6"/></svg>2 FREE dress shirts</li>
        <li class="package__item"><svg class="package__tick" viewBox="0 0 16 16"><path d="M2 9 L6 13 L14 3" fill="none" stroke="#111" stroke-width="1.6"/></svg>2 FREE matching ties</li>
        <li class="package__item"><svg class="package__tick" viewBox="0 0 16 16"><path d="M2 9 L6 13 L14 3" fill="none" stroke="#111" stroke-width="1.6"/></svg>2 FREE leather belts</li>
        <li class="package__item"><svg class="package__tick" viewBox="0 0 16 16"><path d="M2 9 L6 13 L14 3" fill="none" stroke="#111" stroke-width="1.6"/></svg>2 FREE dress socks</li>
      </ul>
    </div>

    <div class="rule rule--top"></div>
    <div class="stock">1000’s of suits in stock<br>SIZES 34 SHORT - 60 LONG<br>Alterations done on premises</div>
    <div class="rule rule--bottom"></div>

    <div class="brand">
      <div class="brand__name">orville</div>
      <div class="brand__sub">menswear</div>
    </div>

    <div class="divider"></div>
    <div class="contact">
      <div class="contact__place">9TH &amp; HOLLOWAY</div>
      <div class="contact__phone">267.555.0148</div>
      <div class="contact__place">BRISTOW GATE PLAZA</div>
      <div class="contact__phone">215.555.0193</div>
      <div class="contact__web">www.orvillemenswear.example</div>
      <div class="contact__legal">Not valid toward previous purchases.<br>Offer may be cancelled and modified<br>at any time.</div>
    </div>
  </section>
</body>
</html>
```